Verelto Services

Double sided business cards with color on front and black and white on back. I have basic ideas and graphics, but am looking for someone to take them to the next level

```html
<!DOCTYPE html>
<html lang="en">
<head>
<meta charset="utf-8">
<title>Verelto Services — Business Card</title>
<link href="https://fonts.googleapis.com/css2?family=Cinzel:wght@400;500&display=swap" rel="stylesheet">
<style>
  :root {
    --canvas-bg: #e4e4e6;
    --card-white: #ffffff;
    --card-black: #000000;
    --ink-blue: #3b3a9c;
    --ink-red: #e21f2b;
    --ink-white: #ffffff;
    --rule-blue: #5a59b0;
    --placeholder-core: #ece8f6;
    --placeholder-edge: #d6d0ec;
    --glow: rgba(255, 255, 255, 0.95);
  }
  * { margin: 0; padding: 0; box-sizing: border-box; }
  html, body {
    width: 1200px;
    height: 900px;
    overflow: hidden;
    background: var(--canvas-bg);
    font-family: "Cinzel", "Times New Roman", serif;
  }
  .canvas {
    position: relative;
    width: 1200px;
    height: 900px;
  }
  .card {
    position: absolute;
    width: 630px;
    height: 360px;
    border-radius: 22px;
    overflow: hidden;
    box-shadow: 0 14px 30px rgba(0, 0, 0, 0.22);
  }

  /* Back side */
  .card-back {
    left: 285px;
    top: 50px;
    background: var(--card-black);
    color: var(--ink-white);
    display: flex;
    flex-direction: column;
    align-items: center;
  }
  .brand-mark {
    margin-top: 52px;
    width: 160px;
    height: 160px;
    border-radius: 50%;
    background: var(--ink-white);
  }
  .tagline {
    margin-top: 26px;
    text-align: center;
    font-size: 17px;
    line-height: 1.35;
    letter-spacing: 1.5px;
    text-transform: uppercase;
  }

  /* Front side */
  .card-front {
    left: 285px;
    top: 470px;
    background:
      radial-gradient(circle at 25% 45%, rgba(200, 190, 235, 0.35) 0%, rgba(255,255,255,0) 55%),
      linear-gradient(120deg, #dcdaf0 0%, #f4f3fb 35%, var(--card-white) 60%);
  }
  .network-art {
    position: absolute;
    left: 30px;
    top: 26px;
    width: 296px;
    height: 296px;
    border-radius: 50%;
    background: radial-gradient(circle, var(--placeholder-core) 0%, var(--placeholder-edge) 100%);
    box-shadow: 0 0 26px 12px var(--glow);
  }
  .wordmark {
    position: absolute;
    left: 346px;
    top: 108px;
    width: 268px;
    text-align: center;
  }
  .wordmark-top {
    display: block;
    font-size: 40px;
    color: var(--ink-blue);
    letter-spacing: 1px;
    line-height: 1;
  }
  .wordmark-bottom {
    display: block;
    font-size: 46px;
    color: var(--ink-red);
    letter-spacing: 1px;
    line-height: 1.05;
  }
  .phone-row {
    display: flex;
    align-items: center;
    gap: 10px;
    margin-top: 6px;
  }
  .phone-row .rule {
    flex: 1;
    height: 1px;
    background: var(--rule-blue);
  }
  .phone {
    font-size: 15px;
    color: var(--ink-blue);
    letter-spacing: 1px;
    white-space: nowrap;
  }
</style>
</head>
<body>
  <main class="canvas">
    <section class="card card-back" aria-label="Back of business card">
      <span class="brand-mark" aria-hidden="true"></span>
      <p class="tagline">A Curated Experience<br>All That Is Promised Is Clarity</p>
    </section>

    <section class="card card-front" aria-label="Front of business card">
      <div class="network-art" role="img" aria-label="Glowing circular network illustration of rainbow dots linked by fine curved lines"></div>
      <div class="wordmark">
        <span class="wordmark-top">VERELTO</span>
        <span class="wordmark-bottom">SERVICES</span>
        <div class="phone-row">
          <span class="rule"></span>
          <span class="phone">P : 555-014-2876</span>
          <span class="rule"></span>
        </div>
      </div>
    </section>
  </main>
</body>
</html>
```